Bellowin Pure Honey

Dear Friends I would like a label to designed for a new brand we wish to create called BELLOWIN pure honey.

I need 2 versions

Version 1 - normal general version for every buyer

Version 2 - this is a KIDS HONEY version and must be designed
specifically to attract Kids and be fun.

Version 1 size is 127mm wide x 60mm high

Version 2 size is 168mm long x 60mm wide

labels must be set up with following info on the face of the product

BELLOWIN

100% Pure Honey

AUSTRALIAN

For version 2 we must have the words KIDS HONEY on the face.

Best regards

Selim

Industry/Entity Type

Product

Requirements
Must have
• Please note the label layout is landscape so 127mm wide x 60mm high

```html
<!DOCTYPE html>
<html lang="en">
<head>
<meta charset="utf-8">
<title>Bellowin Pure Honey – Label</title>
<link href="https://fonts.googleapis.com/css2?family=Poiret+One&family=Kaushan+Script&display=swap" rel="stylesheet">
<style>
  :root {
    --page: #f8f3ec;
    --label: #fdfbf8;
    --ink-brown: #6b4a3e;
    --honey-gold: #d49a0e;
    --honey-orange: #ee6f12;
    --wash-amber: #e9b47a;
    --wash-rust: #c7733a;
    --wash-grey: #c9c3bd;
  }
  html, body {
    margin: 0;
    padding: 0;
    width: 1200px;
    height: 1000px;
    overflow: hidden;
    background: var(--page);
  }
  .canvas {
    position: relative;
    width: 1200px;
    height: 1000px;
    background: var(--page);
  }
  .label {
    position: absolute;
    left: 0;
    top: 232px;
    width: 1200px;
    height: 568px;
    background: var(--label);
    overflow: hidden;
  }
  .label__wildflower-wash {
    position: absolute;
    inset: 0;
    background:
      radial-gradient(ellipse 420px 260px at 160px 470px, rgba(233,180,122,0.55), transparent 70%),
      radial-gradient(ellipse 380px 280px at 1040px 460px, rgba(199,115,58,0.35), transparent 70%),
      radial-gradient(ellipse 520px 240px at 600px 520px, rgba(233,180,122,0.35), transparent 75%),
      linear-gradient(180deg, rgba(255,255,255,0.9) 0%, rgba(240,226,212,0.7) 45%, rgba(232,205,180,0.75) 100%);
  }
  .label__volume {
    position: absolute;
    left: 36px;
    top: 246px;
    margin: 0;
    font-family: "Poiret One", sans-serif;
    font-size: 56px;
    line-height: 1;
    color: var(--ink-brown);
    letter-spacing: -1px;
  }
  .label__purity {
    position: absolute;
    left: 602px;
    top: 330px;
    margin: 0;
    font-family: "Poiret One", sans-serif;
    font-size: 88px;
    line-height: 1;
    color: var(--ink-brown);
  }
  .label__brand {
    position: absolute;
    left: 300px;
    top: 380px;
    width: 600px;
    margin: 0;
    display: flex;
    align-items: center;
    gap: 18px;
    font-family: "Poiret One", sans-serif;
    font-weight: 400;
    font-size: 140px;
    line-height: 1;
    color: var(--honey-gold);
  }
  .label__brand-dot {
    width: 34px;
    height: 34px;
    border-radius: 50%;
    background: var(--honey-gold);
    flex: none;
  }
  .label__product {
    position: absolute;
    left: 345px;
    top: 492px;
    margin: 0;
    font-family: "Kaushan Script", cursive;
    font-size: 82px;
    line-height: 1;
    color: var(--honey-orange);
  }
  .label__origin {
    position: absolute;
    left: 0;
    width: 1200px;
    top: 700px;
    margin: 0;
    text-align: center;
    font-family: "Poiret One", sans-serif;
    font-size: 92px;
    line-height: 1;
    color: var(--ink-brown);
    letter-spacing: -2px;
  }
</style>
</head>
<body>
  <div class="canvas">
    <section class="label">
      <div class="label__wildflower-wash" role="img" aria-label="Soft watercolour field of wild grasses and white daisies in amber and rust tones"></div>
    </section>
    <p class="label__volume">1 litre</p>
    <p class="label__purity">100%</p>
    <h1 class="label__brand">Bellowin<span class="label__brand-dot"></span></h1>
    <p class="label__product">Pure Honey</p>
    <p class="label__origin">AUSTRALIAN</p>
  </div>
</body>
</html>
```